VORTAL Business Card Design

We need a business card for a new company based on the Gold Coast, we are a new supplement distributing company called VORTAL Sports Nutrition - Bold Horizon Sports Nutrition. We are providing new science based bodybuilding and fitness supplementation. Our company has a key focus towards next generation. We are wanting a card that is cool, innovative and fresh. We would like to see the implementation of the below image in a fresh and very innovative design that stands out. The final design should communicate New, Innovative, Cool, Science and researched based.
Target Market(s)
The target market is fitness and bodybuilder enthusiasts. Young audience so very cool looking.
Industry/Entity Type
Fitness
Contact Information for Business Card
(front of card)
VORTAL Sports Nutrition.
Liam Darrow
CEO/Sport Nutrition Specialist
0472 638 904
Liam@vortalsportsfuel.example
www.vortalsportsfuel.example
(back of card)
Scientifically formulated supplement range
Private Nutrition consultations
comprehensive sports nutrition seminars
Requirements
Nice to have
- The card could have a cut out on one of the sides or one of the corners rounded off so the card looks different from a normal business card.
Should not have
- The colours need to complement each other and pop out.

```html
<!DOCTYPE html>
<html lang="en">
<head>
<meta charset="utf-8">
<title>VORTAL Sports Nutrition – Business Card</title>
<link rel="stylesheet" href="https://fonts.googleapis.com/css2?family=Arimo:ital,wght@0,400;0,700;1,400;1,700&display=swap">
<style>
  :root {
    --page-bg: #ffffff;
    --green-top: #9cc44d;
    --green-mid: #7fa242;
    --green-bottom: #4f6b33;
    --text-light: #ffffff;
    --name-red: #a2311f;
    --shadow-dark: rgba(20, 35, 10, 0.75);
    --brand-blue: #5ab8e0;
  }
  html, body {
    margin: 0;
    padding: 0;
    width: 1200px;
    height: 741px;
    overflow: hidden;
    background: var(--page-bg);
  }
  .canvas {
    position: relative;
    width: 1200px;
    height: 741px;
  }
  .card {
    position: absolute;
    left: 46px;
    top: 38px;
    width: 1108px;
    height: 665px;
    border-radius: 32px;
    overflow: hidden;
    font-family: "Arimo", Arial, sans-serif;
  }
  .card-backdrop {
    position: absolute;
    inset: 0;
    background: linear-gradient(180deg, var(--green-top) 0%, var(--green-mid) 50%, var(--green-bottom) 100%);
  }
  .brand {
    position: absolute;
    left: 0;
    right: 0;
    top: 200px;
    display: flex;
    justify-content: center;
    align-items: center;
    gap: 16px;
  }
  .brand-dot {
    width: 36px;
    height: 36px;
    border-radius: 50%;
    background: var(--brand-blue);
  }
  .brand-name {
    font-weight: 700;
    font-size: 72px;
    letter-spacing: 4px;
    color: var(--text-light);
    line-height: 1;
  }
  .tagline {
    position: absolute;
    left: 0;
    right: 0;
    top: 292px;
    text-align: center;
    font-style: italic;
    font-size: 14px;
    color: var(--text-light);
    text-shadow: 0 0 2px #1d2a12, 0 0 2px #1d2a12;
    letter-spacing: 0.2px;
  }
  .contact {
    position: absolute;
    left: 0;
    right: 0;
    top: 454px;
    text-align: center;
    font-weight: 700;
    font-size: 26px;
    line-height: 32px;
    color: var(--text-light);
    text-shadow: 2px 3px 3px var(--shadow-dark);
  }
  .contact p { margin: 0; }
  .contact .person-name {
    color: var(--name-red);
    text-shadow: -1px -1px 0 #fff, 1px -1px 0 #fff, -1px 1px 0 #fff, 1px 1px 0 #fff, 2px 3px 3px var(--shadow-dark);
  }
</style>
</head>
<body>
  <div class="canvas">
    <div class="card">
      <div class="card-backdrop" role="img" aria-label="Green gradient background with faint flowing ornamental pattern"></div>

      <div class="brand">
        <span class="brand-dot"></span>
        <span class="brand-name">VORTAL</span>
      </div>
      <div class="tagline">BOLD HORIZON SPORTS NUTRITION.</div>

      <div class="contact">
        <p class="person-name">Liam Darrow</p>
        <p class="role">CEO/Sport Nutrition Specialist</p>
        <p class="phone">Phone No.: 0472 638 904</p>
        <p class="email">Liam@vortalsportsfuel.example</p>
        <p class="website">www.vortalsportsfuel.example</p>
      </div>
    </div>
  </div>
</body>
</html>
```